Let Us Bloom speaking engagement

the flyer is about a speaking engagement for women's groups. Flyer should be simple, soft, engaging, clean and professional. I am a life coach and also a talk show host. the event I will be advertising is for groups of women. It will be given to church groups, female clubs and organizations. The name of my company is Mara's Lantern Life Coaching Institute.

Target Market(s)

professional women over thirty years old

Font styles to use
Script

Colors
ffffff
34a7d8
85cae6

Requirements
Must have
• use my photo and logo only
Should not have
• anything distracting

```html
<!DOCTYPE html>
<html lang="en">
<head>
<meta charset="UTF-8">
<title>Let Us Bloom – Speaking Engagement Flyer</title>
<link rel="stylesheet" href="https://fonts.googleapis.com/css2?family=Cormorant+Garamond:ital,wght@0,500;1,400&family=Montserrat:wght@400;600;700&display=swap">
<style>
  :root {
    --sky: #34a7d8;
    --sky-deep: #3b94c4;
    --sky-soft: #85cae6;
    --white: #ffffff;
    --gold: #f8d27e;
    --photo-warm: #8a6a4c;
    --photo-dark: #3a2b22;
  }
  html, body {
    margin: 0;
    padding: 0;
    overflow: hidden;
    background: var(--white);
  }
  .flyer {
    position: relative;
    width: 846px;
    height: 1200px;
    overflow: hidden;
    color: var(--white);
    font-family: "Montserrat", sans-serif;
  }
  .backdrop {
    position: absolute;
    inset: 0;
    background:
      radial-gradient(ellipse 380px 520px at 330px 620px, rgba(40,110,160,0.35), transparent 70%),
      radial-gradient(ellipse 300px 300px at 700px 1000px, rgba(40,110,160,0.25), transparent 70%),
      linear-gradient(180deg, var(--sky-deep) 0%, #48a6d6 45%, #3f9ccd 100%);
  }
  .brand-mark {
    position: absolute;
    left: 74px;
    top: 50px;
    width: 240px;
    height: 240px;
    box-sizing: border-box;
    border: 8px solid var(--white);
    border-radius: 50%;
    display: flex;
    align-items: center;
    justify-content: center;
    text-align: center;
  }
  .brand-name {
    font-family: "Montserrat", sans-serif;
    font-weight: 700;
    font-size: 26px;
    line-height: 1.15;
    letter-spacing: 0.5px;
    color: var(--white);
  }
  .divider {
    position: absolute;
    left: 0;
    top: 327px;
    width: 846px;
    height: 7px;
    background: var(--white);
  }
  .portrait-frame {
    position: absolute;
    left: 361px;
    top: 158px;
    width: 346px;
    height: 346px;
    box-sizing: border-box;
    border: 11px solid var(--white);
    transform: rotate(-30deg);
    box-shadow: 6px 8px 10px rgba(20,60,90,0.45);
    background: var(--white);
  }
  .portrait {
    width: 100%;
    height: 100%;
    background:
      radial-gradient(ellipse 60% 55% at 48% 55%, var(--photo-warm), transparent 75%),
      linear-gradient(135deg, #6f5a43 0%, #b99d77 55%, #e9dcc0 100%);
  }
  .headline {
    position: absolute;
    left: 86px;
    top: 390px;
    margin: 0;
    font-weight: 400;
  }
  .headline-intro {
    display: block;
    font-family: "Cormorant Garamond", serif;
    font-style: italic;
    font-size: 44px;
    line-height: 58px;
  }
  .headline-name {
    display: block;
    font-family: "Cormorant Garamond", serif;
    font-weight: 500;
    font-size: 62px;
    line-height: 70px;
    margin-top: -4px;
  }
  .summary {
    position: absolute;
    left: 86px;
    top: 684px;
    width: 680px;
    margin: 0;
    font-size: 20px;
    line-height: 30px;
    font-weight: 400;
  }
  .summary strong {
    font-weight: 700;
  }
  .invite-band {
    position: absolute;
    left: 0;
    top: 856px;
    width: 846px;
    height: 126px;
    background: var(--sky-soft);
    display: flex;
    align-items: center;
    justify-content: center;
    text-align: center;
  }
  .invite-text {
    margin: 0;
    font-weight: 700;
    font-size: 30px;
    line-height: 44px;
  }
  .contact {
    position: absolute;
    left: 0;
    top: 992px;
    width: 846px;
    text-align: center;
    color: var(--gold);
    font-weight: 700;
  }
  .contact-label {
    margin: 0;
    font-size: 31px;
    line-height: 44px;
  }
  .contact-numbers {
    margin: 0;
    font-size: 45px;
    line-height: 56px;
  }
</style>
</head>
<body>
  <main class="flyer">
    <div class="backdrop" role="img" aria-label="Soft blue-tinted background portrait of the life coach"></div>

    <div class="brand-mark">
      <span class="brand-name">MARA'S<br>LANTERN</span>
    </div>

    <div class="divider"></div>

    <div class="portrait-frame">
      <div class="portrait" role="img" aria-label="Smiling headshot photo of life coach Talia Morrow"></div>
    </div>

    <h1 class="headline">
      <span class="headline-intro">A heart to heart</span>
      <span class="headline-intro">conversation</span>
      <span class="headline-intro">with Life Coach</span>
      <span class="headline-name">Talia Morrow</span>
    </h1>

    <p class="summary"><strong>Let Us Bloom</strong> is an interactive soul searching session that will help women share their stories and be real about the things that matter most.</p>

    <section class="invite-band">
      <p class="invite-text">To invite Talia<br>to your women's group or gathering</p>
    </section>

    <section class="contact">
      <p class="contact-label">Contact us at</p>
      <p class="contact-numbers">242-555-0148 or 555-0193</p>
    </section>
  </main>
</body>
</html>
```